A wine Label for a new brand of New Zealand Wine

We are looking for a Wine Label for our "Harbor Crest" brand of wines from North Otago New Zealand. We would like the label to perhaps use the HC as a logo and the rest up to the designer. We have our vineyards located in the Waitaki Valley New Zealand which is a southern region with mountains and a river flowing past our vineyard. Photos attached of Dramatic Landscape. Also attached is a basic outline of requirements for the front bottle of the label. The rear bottle label will contain writing about the wines background plus statutory regulations on Alc. Vol, bar code etc. Front Label size to be no Larger than 80mm deep by 100 mm wide. The label can be simple or graphic, whatever the designer chooses.
Target Market(s)
New Wine Brand
Look and feel
Each slider illustrates characteristics of the customer's brand and the style your logo design should communicate.

```html
<!DOCTYPE html>
<html lang="en">
<head>
<meta charset="utf-8">
<title>Harbor Crest – Pinot Gris Label</title>
<link rel="stylesheet" href="https://fonts.googleapis.com/css2?family=Cinzel:wght@600&family=EB+Garamond:ital,wght@0,400;1,400&family=Josefin+Sans:wght@300;400&display=swap">
<style>
  :root {
    --page-bg: #ededed;
    --sky-top: #4fa8c8;
    --sky-mid: #8fcbd2;
    --field-light: #eef0b8;
    --field-pale: #f6f2c4;
    --hill-tone: #a9c9b4;
    --vine-tone: #8fae86;
    --gold-text: #f4ec9c;
    --ink-dark: #2f4a45;
    --ink-olive: #4d5a36;
  }
  * { margin: 0; padding: 0; box-sizing: border-box; }
  html, body {
    width: 1200px;
    height: 972px;
    overflow: hidden;
    background: var(--page-bg);
  }
  .canvas {
    position: relative;
    width: 1200px;
    height: 972px;
  }
  .wine-label {
    position: absolute;
    left: 200px;
    top: 46px;
    width: 800px;
    height: 880px;
    overflow: hidden;
    background: linear-gradient(180deg, var(--sky-top) 0%, var(--sky-mid) 45%, var(--field-light) 78%, var(--field-pale) 100%);
    box-shadow: 0 6px 24px rgba(0,0,0,0.12);
  }
  .landscape {
    position: absolute;
    left: 0;
    top: 400px;
    width: 100%;
    height: 400px;
    background:
      linear-gradient(180deg, rgba(143,203,210,0) 0%, rgba(169,201,180,0.75) 30%, rgba(143,174,134,0.7) 55%, rgba(238,240,184,0.8) 85%, rgba(246,242,196,0) 100%);
  }
  .brand-mark {
    position: absolute;
    left: 50%;
    top: 62px;
    width: 140px;
    height: 140px;
    margin-left: -70px;
    border: 3px solid var(--gold-text);
    display: flex;
    align-items: center;
    justify-content: center;
    font-family: "Cinzel", serif;
    font-weight: 600;
    font-size: 64px;
    color: var(--gold-text);
  }
  .brand-name {
    position: absolute;
    top: 232px;
    width: 100%;
    text-align: center;
    font-family: "Cinzel", serif;
    font-weight: 600;
    font-size: 84px;
    letter-spacing: 2px;
    color: var(--gold-text);
  }
  .varietal {
    position: absolute;
    top: 340px;
    width: 100%;
    text-align: center;
    font-family: "Josefin Sans", sans-serif;
    font-weight: 300;
    font-size: 34px;
    letter-spacing: 7px;
    color: var(--ink-dark);
  }
  .vintage {
    position: absolute;
    top: 386px;
    width: 100%;
    text-align: center;
    font-family: "Josefin Sans", sans-serif;
    font-weight: 400;
    font-size: 28px;
    letter-spacing: 2px;
    color: var(--ink-dark);
  }
  .origin {
    position: absolute;
    top: 752px;
    width: 100%;
    text-align: center;
    font-family: "EB Garamond", serif;
    font-style: italic;
    font-size: 32px;
    color: var(--ink-olive);
  }
  .region {
    position: absolute;
    top: 800px;
    width: 100%;
    text-align: center;
    font-family: "EB Garamond", serif;
    font-size: 28px;
    letter-spacing: 2px;
    color: var(--ink-olive);
  }
</style>
</head>
<body>
<div class="canvas">
  <section class="wine-label">
    <div class="landscape" role="img" aria-label="Photograph of mountains above vineyards in the valley"></div>
    <div class="brand-mark">HC</div>
    <h1 class="brand-name">Harbor Crest</h1>
    <p class="varietal">PINOT GRIS</p>
    <p class="vintage">2015</p>
    <p class="origin">New Zealand Wine</p>
    <p class="region">WAITAKI VALLEY—NORTH OTAGO</p>
  </section>
</div>
</body>
</html>
```